Flyer-Design für Amerikanische Chiropraktik
Zielgruppe
Praxis für Amerikanische Chiropraktik
Zielgruppe: Gesundheitsbewusste Menschen, gerne gebildet, Affinität zu Sport/Yoga etc.
Flyer soll modern und hochwertig sein (Zielgruppe auch Privatversicherte und Büroleute)
Aufgabenstellung
Bitte keine Schnörkel.
Klare Linien. Straight einfach
Positive Vibes
Website ist nicht final fertig. Das blau/grau und das Grün wird aber aller Voraussicht nach Weiter verwendet. Falls das rot verwendet wird eher nicht so oft bitte.
Sehr gerne für die Überschriften die gleichen Balken unter den Überschriften für den Flyer verwenden.
Flyer bei Nordra Druck ist 99x210 mm (ich denke mit etwas Spiel am Rand für den Druck.) 6 Seiten.
Auf der letzten Seite (sollte die mittlere Rückseite sein) bitte Kontaktdaten und evtl Portraitbild.

```html
<!DOCTYPE html>
<html lang="de">
<head>
<meta charset="utf-8">
<title>Chiropraktik Kasimir Holt – Flyer</title>
<link rel="stylesheet" href="https://fonts.googleapis.com/css2?family=Raleway:wght@300;400;500&display=swap">
<style>
  :root {
    --dark: #3d3d3f;
    --paper: #e0e0e0;
    --blue: #2b8fc6;
    --text: #555557;
    --text-light: #e6e6e6;
    --rule: #9a9a9c;
    --rose: #d9c2b8;
    --ink: #222224;
  }
  * { margin: 0; padding: 0; box-sizing: border-box; }
  html, body { width: 1200px; height: 600px; overflow: hidden; }
  body {
    position: relative;
    background: var(--paper);
    font-family: "Raleway", sans-serif;
    font-weight: 300;
    color: var(--text);
    font-size: 10px;
  }
  .abs { position: absolute; }
  .heading {
    position: absolute;
    color: var(--blue);
    font-weight: 400;
    font-size: 14.5px;
    line-height: 1.25;
    white-space: nowrap;
  }
  .photo { position: absolute; }

  /* left panel */
  .intro-panel { left: 0; top: 0; width: 300px; height: 413px; background: var(--dark); }
  .bottom-band { left: 0; top: 543px; width: 1200px; height: 57px; background: var(--dark); }
  .portrait { left: 27px; top: 62px; width: 76px; height: 113px; background: linear-gradient(160deg, #e2b48f, #cfa07c 55%, #efe9e4); }
  .owner { left: 141px; top: 137px; color: var(--text-light); font-size: 10px; line-height: 14px; }
  .owner-name { color: var(--blue); font-weight: 400; }
  .checklist { left: 27px; top: 203px; list-style: none; color: var(--text-light); font-weight: 400; font-size: 10px; line-height: 14.3px; white-space: nowrap; }
  .checklist li { position: relative; padding-left: 22px; margin-bottom: 13.6px; }
  .checklist svg { position: absolute; left: 0; top: 3px; }
  .brand { left: 0; top: 440px; width: 294px; text-align: center; }
  .brand-dot { display: block; margin: 0 auto 12px; width: 46px; height: 46px; border: 1.5px solid var(--ink); border-radius: 50%; }
  .brand-name { color: var(--ink); font-weight: 400; font-size: 14px; letter-spacing: 1px; }
  .contact { left: 36px; top: 553px; color: #cfcfcf; font-size: 10px; line-height: 14px; }
  .contact span { margin-right: 12px; }

  .rule { position: absolute; width: 1px; background: var(--rule); }

  /* column 2 */
  .col2-text { left: 333px; top: 62px; width: 234px; text-align: justify; line-height: 14.2px; hyphens: manual; }
  .sub { left: 333px; top: 161px; font-weight: 400; font-size: 10px; }
  .fields { left: 333px; top: 186px; list-style: none; line-height: 16.1px; white-space: nowrap; }
  .fields li { position: relative; padding-left: 36px; }
  .fields li::before { content: "•"; position: absolute; left: 0; font-size: 7px; }
  .col2-photo { left: 333px; top: 360px; width: 234px; height: 205px; background: linear-gradient(150deg, #f0cfb6, #e6b896 60%, #d9cfd2); }

  /* column 3 */
  .lead { left: 632px; top: 60px; width: 234px; text-align: justify; text-align-last: justify; }
  .benefits { left: 632px; top: 104px; width: 234px; display: flex; justify-content: space-between; line-height: 16.15px; }
  .benefits ul { list-style: none; }
  .benefits .right { text-align: right; }
  .benefits .label { font-weight: 500; letter-spacing: 0.6px; color: #444; }
  .ellipse { left: 616px; top: 313px; }
  .joints { left: 646px; top: 357px; line-height: 16.1px; white-space: nowrap; }
  .joints .heading { position: static; margin-bottom: 5px; margin-left: 6px; }
  .joints ul { list-style: none; }
  .joints li { position: relative; padding-left: 7px; }
  .joints li::before { content: "•"; position: absolute; left: 0; font-size: 8px; }
  .joints b { font-weight: 500; color: #3a3a3c; }

  /* column 4 */
  .col4-photo { left: 932px; top: 34px; width: 125px; height: 164px; background: linear-gradient(160deg, #e8bfa2, #dcb395 55%, #d9c4c8); }
  .reasons { left: 932px; top: 272px; list-style: none; line-height: 16.15px; }
  .reasons li { position: relative; padding-left: 6px; }
  .reasons li::before { content: "•"; position: absolute; left: 0; font-size: 7px; }
  .col4-photo2 { left: 1040px; top: 401px; width: 126px; height: 164px; background: linear-gradient(180deg, #ededeb, #e8d7c6 50%, #dcc2c6); }
</style>
</head>
<body>
  <div class="abs intro-panel"></div>
  <div class="abs bottom-band"></div>

  <h2 class="heading" style="left:27px; top:32px;">WIR FREUEN UNS AUF DICH!</h2>
  <div class="photo portrait" role="img" aria-label="Porträtfoto des Chiropraktikers"></div>
  <p class="abs owner"><span class="owner-name">KASIMIR HOLT</span><br>Heil- und Chiropraktiker,<br>B.Sc. Physiotherapie</p>

  <ul class="abs checklist">
    <li><svg width="12" height="13" viewBox="0 0 12 13"><path d="M1 8 L4 12 L11 1" fill="none" stroke="#2b8fc6" stroke-width="1.3"/></svg>Wir sind Experten auf unserem Gebiet.</li>
    <li><svg width="12" height="13" viewBox="0 0 12 13"><path d="M1 8 L4 12 L11 1" fill="none" stroke="#2b8fc6" stroke-width="1.3"/></svg>Arbeiten nach neuesten Wissenschaftlichen<br>Kenntnissen.</li>
    <li><svg width="12" height="13" viewBox="0 0 12 13"><path d="M1 8 L4 12 L11 1" fill="none" stroke="#2b8fc6" stroke-width="1.3"/></svg>Sanfte und zielgerichtete Behandlung.</li>
    <li><svg width="12" height="13" viewBox="0 0 12 13"><path d="M1 8 L4 12 L11 1" fill="none" stroke="#2b8fc6" stroke-width="1.3"/></svg>Profitieren Sie von langjährige praktische<br>Erfahrung und modernen neurowissenschaftliche<br>Aspekten in der chiropraktischen Behandlung.</li>
    <li><svg width="12" height="13" viewBox="0 0 12 13"><path d="M1 8 L4 12 L11 1" fill="none" stroke="#2b8fc6" stroke-width="1.3"/></svg>Wir sind mit Freude und Engagement für Dich<br>und Deine Gesundheit da.</li>
  </ul>

  <div class="abs brand">
    <span class="brand-dot"></span>
    <div class="brand-name">KASIMIR HOLT</div>
  </div>

  <p class="abs contact"><span>Chiropraxis Holt</span><span>Lindenweg 4</span>83629 Auenried<br><span>Tel: 0151/48261937</span>www.chiropraktik-holt.de</p>

  <div class="rule" style="left:301px; top:40px; height:537px;"></div>
  <div class="rule" style="left:600px; top:46px; height:497px;"></div>
  <div class="rule" style="left:901px; top:32px; height:537px;"></div>

  <h2 class="heading" style="left:333px; top:32px;">FÜR WEN?</h2>
  <p class="abs col2-text">Die Amerikanische Chiropraktik verfolgt einen ganz&shy;heitlichen und ursachenbezogenen Ansatz, wodurch sich vielseitige Anwendungsbereiche ergeben. Unser Angebot reicht von Gesundheitsvorsorge bis hin zur Behandlung von bereits existierenden Störungen und Symptomen.</p>
  <p class="abs sub">Anwendungsgebiete</p>
  <ul class="abs fields">
    <li>Chiropraktik zur Leistungssteigerung im<br>Sport</li>
    <li>Chiropraktik als konstante Begleitung für<br>mehr Balance und Wohlbefinden im Alltag</li>
    <li>Chiropraktik in der Schwangerschaft</li>
    <li>Chiropraktik als effektive Methode für die<br>Behandlung von Schmerzen und Einschrän-<br>kungen des Bewegungsapparats und des<br>Nervensystems</li>
  </ul>
  <div class="photo col2-photo" role="img" aria-label="Foto: Chiropraktiker behandelt eine Patientin im Sitzen"></div>

  <h2 class="heading" style="left:632px; top:32px;">IHRE VORTEILE MIT CHIROPRAKTIK</h2>
  <p class="abs lead">Mit unserem ganzheitlichen Ansatz wollen wir</p>
  <div class="abs benefits">
    <ul>
      <li class="label">REDUZIEREN</li>
      <li>Müdigkeit</li><li>Fehlhaltungen</li><li>Verletzungen</li><li>Konzentrationsstörungen</li><li>Schlafstörungen</li><li>Verspannungen</li><li>Eingeschränkte</li><li>Beweglichkeit</li><li>Schmerz</li><li>Krankheit</li><li>Stress</li>
    </ul>
    <ul class="right">
      <li class="label">VERBESSERN</li>
      <li>Leistungssteigerung</li><li>Innere Ausgeglichenheit</li><li>Stressresistenz</li><li>Beweglichkeit</li><li>Gesundheit</li><li>Schlaf</li><li>Glücksgefühl</li><li>Kreislaufsystem</li><li>Kraft</li><li>Aktive Lebensweise</li><li>Konzentration</li>
    </ul>
  </div>

  <svg class="abs ellipse" width="276" height="221" viewBox="0 0 276 221"><ellipse cx="138" cy="110.5" rx="136.5" ry="109" fill="none" stroke="var(--rose)" stroke-width="1.6"/></svg>
  <div class="abs joints">
    <h2 class="heading">CHIROPRAKTIK UND GELENKE</h2>
    <ul>
      <li><b>Beweglicher!</b> Wir erzeugen schelle Dehnungen<br>der Muskulatur direkt am Gelenk und nehmen<br>den Druck.</li>
      <li><b>Leichter!</b> Dabei lösen wir Reflexe aus, die im<br>Gehirn die Funktion zurückbringen.</li>
      <li><b>Besser!</b> Unterstützt die Heilung deiner Gelenke<br>und Nervensystem</li>
    </ul>
  </div>

  <div class="photo col4-photo" role="img" aria-label="Foto: Chiropraktiker umfasst eine Patientin zur Behandlung"></div>
  <h2 class="heading" style="left:932px; top:226px;">DAHER BESUCHEN UNS<br>MENSCHEN MIT:</h2>
  <ul class="abs reasons">
    <li>Chronischer Stress</li><li>Schwindel</li><li>Müdigkeit</li><li>Kopfschmerzen</li><li>Migräne</li><li>Schulter- und Armschmerzen</li><li>Impingement-Syndrom</li><li>Karpaltunnelsyndrom</li><li>Beckenschiefstand</li><li>Tinnitus</li><li>Rückenschmerzen</li><li>Bandscheibenvorfall</li><li>Kribbeln und Taubheit<br>in Händen oder Füßen</li>
  </ul>
  <div class="photo col4-photo2" role="img" aria-label="Foto: entspannte Patientin liegt bei einer Kopfbehandlung"></div>
</body>
</html>
```